Job site for plomvarinex.com

Update: Looking for a really simple design that is fit for a short attention span.
Need a website built that I can host on Brimfoxa.com.
Need tracking: Important to track where students are clicking and be able to provide that detail to employers.
The site will use the plomvarinex.com logo (attached).
Add a tagline - Highschool Students Start Here
( Link on main page) Job Opportunities (click to page)
- Listing of new jobs.
o Job Title
o Company Name
o Position Description
o Hyperlink to employer website (need to be able to track clicks)
(Link on main page) Tools & Career Advice (click to page)
o This section would allow for the posting of advice and articles.
(Link on main page) Ask a Job Question? (click to page)
o Submit a question via email – email only collected. No personal
info.
(Link on main page) Volunteer Opportunities (click to page)
o A listing of organizations that need student volunteers. Need
to be able to add a new listing. Similar to a job listing:
Business or Non-profit Name
Description of need
Hyperlink to website or simply contact info.
(Link on main page) About Us
- Be able to change the content
Updates
Target Market(s)
Ages 14-18
Industry/Entity Type
job board
Coding
Coded - Design and coding required
Number of Pages Required
4 page
Look and feel

```html
<!DOCTYPE html>
<html lang="en">
<head>
<meta charset="utf-8">
<title>plomvarinex.com — Highschool Students Start Here</title>
<link href="https://fonts.googleapis.com/css2?family=Roboto:wght@300;400;500;700&display=swap" rel="stylesheet">
<style>
:root{
  --sky:#2fb9e6;
  --sky-light:#8fdcf5;
  --sky-deep:#17a6dc;
  --heading-blue:#1aa3dc;
  --orange:#f7941d;
  --ink:#1e1e1e;
  --muted:#666;
  --line:#e6e6e6;
  --white:#fff;
  --cream:#fff7ef;
}
*{box-sizing:border-box;margin:0;padding:0}
html,body{width:1200px;height:4213px;overflow:hidden}
body{position:relative;font-family:'Roboto',Arial,sans-serif;color:var(--ink);background:var(--white)}
.abs{position:absolute}
a{color:inherit;text-decoration:none}

/* hero */
.hero{left:0;top:0;width:1200px;height:660px;background:linear-gradient(160deg,#27b4e4 0%,#55c8ee 55%,#a7e3f7 100%);overflow:hidden}
.brand{display:flex;align-items:center;gap:10px;color:var(--white);font-weight:500;font-size:22px}
.brand .dot{width:34px;height:34px;border-radius:50%;background:var(--white)}
.brand small{display:block;font-size:9px;font-weight:400;letter-spacing:.5px}
.nav{left:355px;top:42px;display:flex;gap:30px;font-size:14px;color:var(--white)}
.nav a.active{border-bottom:1px solid var(--white);padding-bottom:3px}
.vert{transform:rotate(-90deg);transform-origin:left top;color:rgba(255,255,255,.35);font-size:44px;font-weight:300;letter-spacing:2px;white-space:nowrap}
.hero h1{left:136px;top:218px;color:var(--white);font-size:62px;line-height:60px;font-weight:300}
.hero h1 b{font-weight:700}
.btn{display:inline-flex;align-items:center;justify-content:center;background:var(--orange);color:var(--white);font-weight:700;font-size:14px;border-radius:24px;text-transform:uppercase}
.chip{display:flex;align-items:center;gap:8px;height:46px;padding:0 8px 0 12px;border:1px solid rgba(255,255,255,.7);border-radius:24px;background:rgba(255,255,255,.12);color:var(--white)}
.chip .txt{font-size:11px;line-height:18px}
.chip .txt span{float:right;margin-left:22px}
.chip .txt em{display:block;font-style:normal;font-size:8px}
.chip .mk{width:34px;height:34px;border-radius:50%;background:var(--white)}
.ph{border-radius:6px}

/* headings */
.sec-title{width:1200px;text-align:center;font-size:39px;font-weight:300;color:var(--ink)}
.sec-title b{font-weight:500;color:var(--heading-blue)}
.sec-title .cap{display:inline-block;width:44px;height:10px;background:var(--sky);transform:skew(-20deg) translateY(-30px);margin-right:-30px;border-radius:2px}

/* cards */
.card{width:319px;height:224px;background:var(--white);border:1px solid var(--line);border-radius:4px;box-shadow:0 2px 6px rgba(0,0,0,.06);padding:20px 15px}
.card .hd{display:flex;gap:10px;align-items:center}
.card .logo{width:42px;height:42px;border-radius:50%;background:#222}
.card .name{font-size:13px;font-weight:700}
.card .loc{font-size:10px;color:var(--muted);margin-top:3px}
.card h3{font-size:14px;font-weight:500;margin:22px 0 8px}
.card p{font-size:10px;line-height:18px;color:#444}
.card .ft{position:absolute;left:15px;right:15px;bottom:14px;display:flex;align-items:center;font-size:12px}
.card .visit{color:var(--heading-blue);width:110px}
.card .time{flex:1}
.card .dots{font-size:20px;letter-spacing:1px;font-weight:700;line-height:10px}
.vcard p{font-size:12px;line-height:23px;margin-top:18px}
.vcard .visit{text-decoration:underline}

.field{border:1px solid #cfcfcf;border-radius:4px;background:var(--white);font-size:12px;color:#333;padding:0 20px;display:flex;align-items:center}

/* tools */
.tools-bg{left:0;top:1500px;width:1200px;height:730px}
.post-meta{font-size:11px;color:rgba(255,255,255,.9)}
.post-title{color:var(--white);font-size:16px;font-weight:500;line-height:20px}
.post-text{color:rgba(255,255,255,.92);font-size:12px;line-height:19px}
.more{color:var(--white);font-size:13px;font-weight:700}
.side{left:777px;width:220px}
.rule{left:625px;width:374px;height:1px;background:rgba(255,255,255,.5)}

/* ask */
.ask{left:185px;top:2224px;width:832px;height:372px;background:var(--white);border-radius:8px;box-shadow:0 4px 18px rgba(0,0,0,.08)}
.mini-cap{display:inline-block;width:40px;height:9px;background:var(--sky);transform:skew(-20deg) translateY(-28px);margin-right:-30px;border-radius:2px}

/* about */
.about-bg{left:0;top:3000px;width:1200px;height:760px;background:linear-gradient(180deg,#fff 0%,var(--cream) 40%,#fff 100%)}
.about p{font-size:13px;line-height:26px;color:#444}

/* footer */
.footer{left:0;top:3700px;width:1200px;height:513px}
.fcol h4{font-size:21px;font-weight:500;color:var(--white);margin-bottom:10px}
.fcol a{display:block;font-size:14px;color:var(--white);line-height:32px}
.contact{display:flex;align-items:center;gap:12px;color:var(--white);font-size:14px;margin-bottom:20px}
.contact .ic{width:36px;height:36px;border:1.5px solid var(--white);border-radius:50%;display:flex;align-items:center;justify-content:center;flex:none}
.social{width:36px;height:36px;border:1.5px solid var(--white);border-radius:50%}
</style>
</head>
<body>

<!-- HERO -->
<section class="abs hero">
  <svg class="abs" style="left:0;top:0" width="1200" height="660" viewBox="0 0 1200 660" aria-hidden="true">
    <circle cx="338" cy="122" r="22" fill="rgba(255,255,255,.18)"/>
    <circle cx="834" cy="376" r="262" fill="none" stroke="rgba(255,255,255,.55)" stroke-width="1.5"/>
    <circle cx="834" cy="114" r="6" fill="#1f8fc7"/>
    <circle cx="690" cy="350" r="6" fill="#1f8fc7"/>
    <path d="M0 565 C200 540 330 600 520 585 C700 570 880 610 1200 560 L1200 660 L0 660Z" fill="rgba(255,255,255,.35)"/>
    <path d="M0 600 C220 580 360 630 560 620 C760 610 920 640 1200 600 L1200 660 L0 660Z" fill="#fff"/>
  </svg>
  <div class="abs brand" style="left:98px;top:95px">
    <span class="dot"></span>
    <span>plomvarinex.com<small>Jobs | Tools | Success</small></span>
  </div>
  <nav class="abs nav">
    <a class="active" href="#jobs">Job Opportunities</a>
    <a href="#tools">Tools &amp; Career Advice</a>
    <a href="#ask">Ask a Job Question?</a>
    <a href="#volunteer">Volunteer Opportunities</a>
    <a href="#about">About Us</a>
  </nav>
  <div class="abs vert" style="left:24px;top:492px">PLOMVARINEX</div>
  <h1 class="abs">Highschool<br><b>Students Start<br>Here</b></h1>
  <a class="abs btn" style="left:126px;top:419px;width:204px;height:44px" href="#jobs">Job Opportunities</a>

  <div class="abs chip" style="left:606px;top:124px;width:194px"><div class="txt">Job Title <span>Ocircle</span><em>Lorem ipsum dolor sitnsectetur</em></div><i class="mk"></i></div>
  <div class="abs chip" style="left:878px;top:124px;width:198px"><i class="mk"></i><div class="txt">Job Title <span>Ocircle</span><em>Lorem ipsum dolor sitnsectetur</em></div></div>
  <div class="abs chip" style="left:540px;top:211px;width:194px"><div class="txt">Job Title <span>Ocircle</span><em>Lorem ipsum dolor sitnsectetur</em></div><i class="mk"></i></div>
  <div class="abs chip" style="left:948px;top:211px;width:196px"><i class="mk"></i><div class="txt">Job Title <span>Ocircle</span><em>Lorem ipsum dolor sitnsectetur</em></div></div>

  <div class="abs ph" role="img" aria-label="Smiling student sitting cross-legged with a laptop" style="left:621px;top:180px;width:295px;height:460px;background:linear-gradient(180deg,#c46a5a 0%,#d9b79a 60%,#e8dccd 100%);opacity:.85"></div>
  <div class="abs ph" role="img" aria-label="Potted green plant" style="left:490px;top:392px;width:131px;height:254px;background:linear-gradient(180deg,#4f8f3a 0%,#6aa64a 65%,#eeeeee 66%,#dcdcdc 100%)"></div>
  <div class="abs ph" role="img" aria-label="White coffee mug" style="left:1014px;top:548px;width:90px;height:90px;background:linear-gradient(180deg,#f7f7f7,#d9d9d9);border-radius:12px"></div>
</section>

<!-- JOBS -->
<h2 class="abs sec-title" id="jobs" style="top:725px"><span class="cap"></span>Job <b>Opportunities</b></h2>

<div class="abs card" style="left:101px;top:806px"><div class="hd"><i class="logo"></i><div><div class="name">Stay Radiant</div><div class="loc">&#9679; Location Name</div></div></div><h3>Graphic Designer</h3><p>Lorem ipsum dolor sit amet,adipislit, sed do eiusmod tempor incididunt utbore et dolore magna aliqua.Lorem ipsum dolor sit Lorem ipsum dolor sit amet,adipis</p><div class="ft"><a class="visit" href="#">&#9678; Visit Site &raquo;</a><span class="time">&#9719; 11 hours ago</span><span class="dots">&bull;&bull;&bull;</span></div></div>
<div class="abs card" style="left:440px;top:806px"><div class="hd"><i class="logo" style="background:#19c46a"></i><div><div class="name">Stay Radiant</div><div class="loc">&#9679; Location Name</div></div></div><h3>Graphic Designer</h3><p>Lorem ipsum dolor sit amet,adipislit, sed do eiusmod tempor incididunt utbore et dolore magna aliqua.Lorem ipsum dolor sit Lorem ipsum dolor sit amet,adipis</p><div class="ft"><a class="visit" href="#">&#9678; Visit Site &raquo;</a><span class="time">&#9719; 11 hours ago</span><span class="dots">&bull;&bull;&bull;</span></div></div>
<div class="abs card" style="left:778px;top:806px"><div class="hd"><i class="logo" style="background:#6a3fc9"></i><div><div class="name">Stay Radiant</div><div class="loc">&#9679; Location Name</div></div></div><h3>Graphic Designer</h3><p>Lorem ipsum dolor sit amet,adipislit, sed do eiusmod tempor incididunt utbore et dolore magna aliqua.Lorem ipsum dolor sit Lorem ipsum dolor sit amet,adipis</p><div class="ft"><a class="visit" href="#">&#9678; Visit Site &raquo;</a><span class="time">&#9719; 11 hours ago</span><span class="dots">&bull;&bull;&bull;</span></div></div>
<div class="abs card" style="left:101px;top:1048px"><div class="hd"><i class="logo" style="background:#2b3a4a"></i><div><div class="name">Stay Radiant</div><div class="loc">&#9679; Location Name</div></div></div><h3>Graphic Designer</h3><p>Lorem ipsum dolor sit amet,adipislit, sed do eiusmod tempor incididunt utbore et dolore magna aliqua.Lorem ipsum dolor sit Lorem ipsum dolor sit amet,adipis</p><div class="ft"><a class="visit" href="#">&#9678; Visit Site &raquo;</a><span class="time">&#9719; 11 hours ago</span><span class="dots">&bull;&bull;&bull;</span></div></div>
<div class="abs card" style="left:440px;top:1048px"><div class="hd"><i class="logo"></i><div><div class="name">Stay Radiant</div><div class="loc">&#9679; Location Name</div></div></div><h3>Graphic Designer</h3><p>Lorem ipsum dolor sit amet,adipislit, sed do eiusmod tempor incididunt utbore et dolore magna aliqua.Lorem ipsum dolor sit Lorem ipsum dolor sit amet,adipis</p><div class="ft"><a class="visit" href="#">&#9678; Visit Site &raquo;</a><span class="time">&#9719; 11 hours ago</span><span class="dots">&bull;&bull;&bull;</span></div></div>
<div class="abs card" style="left:778px;top:1048px"><div class="hd"><i class="logo" style="background:#333"></i><div><div class="name">Stay Radiant</div><div class="loc">&#9679; Location Name</div></div></div><h3>Graphic Designer</h3><p>Lorem ipsum dolor sit amet,adipislit, sed do eiusmod tempor incididunt utbore et dolore magna aliqua.Lorem ipsum dolor sit Lorem ipsum dolor sit amet,adipis</p><div class="ft"><a class="visit" href="#">&#9678; Visit Site &raquo;</a><span class="time">&#9719; 11 hours ago</span><span class="dots">&bull;&bull;&bull;</span></div></div>

<!-- NEWSLETTER -->
<h2 class="abs sec-title" style="top:1346px;font-size:28px"><span class="cap" style="transform:skew(-20deg) translateY(-22px)"></span>Signup for Newsletter and &nbsp;<b>New Job Postings</b></h2>
<div class="abs field" style="left:316px;top:1410px;width:373px;height:42px;border-radius:22px">Email Address</div>
<a class="abs btn" style="left:697px;top:1410px;width:188px;height:42px" href="#">Submit</a>

<!-- TOOLS -->
<svg class="abs tools-bg" viewBox="0 0 1200 730" width="1200" height="730" aria-hidden="true">
  <defs><linearGradient id="tg" x1="0" y1="0" x2="1" y2="1"><stop offset="0" stop-color="#2ab6e5"/><stop offset="1" stop-color="#7fd3f1"/></linearGradient></defs>
  <path d="M0 40 C250 20 500 100 760 80 C950 65 1080 40 1200 60 L1200 690 C1000 720 800 700 600 712 C400 724 200 700 0 716Z" fill="url(#tg)"/>
  <rect x="40" y="70" width="70" height="70" rx="14" fill="rgba(255,255,255,.12)"/>
  <circle cx="1080" cy="280" r="22" fill="rgba(255,255,255,.18)"/>
</svg>
<div class="abs vert" style="left:24px;top:2180px;font-size:40px">TOOLS &amp; CAREER ADVICE</div>
<h2 class="abs sec-title" id="tools" style="top:1666px;color:var(--white)"><span class="cap" style="background:var(--white)"></span>Tools &amp; <b style="color:var(--white);font-weight:700">Career Advice</b></h2>

<div class="abs ph" role="img" aria-label="Students working together around a laptop in a library" style="left:201px;top:1734px;width:404px;height:234px;background:linear-gradient(135deg,#4b5a70,#a89a86 60%,#d6cfc3);border-radius:0"></div>
<div class="abs post-meta" style="left:201px;top:1991px">&#9679; Plomvarinex &nbsp;&nbsp;&nbsp;&nbsp; | &nbsp;&nbsp;&nbsp; &#9719; Dec 18 ,2020</div>
<div class="abs post-title" style="left:201px;top:2021px;width:400px">Lorem ipsum dolor sit amet, consectetur adipiscing elit, sed do eiusmod tempor</div>
<div class="abs post-text" style="left:201px;top:2077px;width:390px;font-size:11.5px">Lorem ipsum dolor sit amet, consectetur adipiscing elit, sed do eiusmod tempor incididunt ut labore et dolore magna aliquis ipsum suspendisse ultrices gravida. Risus commodo viverra maecenas accumsan lacus vel facilisis.</div>
<div class="abs more" style="left:201px;top:2170px">Continue Reading...</div>

<div class="abs ph" role="img" aria-label="Group of students chatting" style="left:625px;top:1735px;width:127px;height:126px;background:linear-gradient(135deg,#7a5a4a,#c9b3a0);border-radius:0"></div>
<div class="abs side post-meta" style="top:1747px">&#9679; Plomvarinex &nbsp;&nbsp; | &nbsp; &#9719; Dec 18 ,2020</div>
<div class="abs side post-title" style="top:1772px">Lorem ipsum dolor sit amet, consectetur adipiscing</div>
<div class="abs side more" style="top:1833px">Continue Reading...</div>
<div class="abs rule" style="top:1880px"></div>

<div class="abs ph" role="img" aria-label="Student holding books outdoors" style="left:625px;top:1899px;width:127px;height:126px;background:linear-gradient(135deg,#4d7a5a,#b7a48a);border-radius:0"></div>
<div class="abs side post-meta" style="top:1910px">&#9679; Plomvarinex &nbsp;&nbsp; | &nbsp; &#9719; Dec 18 ,2020</div>
<div class="abs side post-title" style="top:1935px">Lorem ipsum dolor sit amet, consectetur adipiscing</div>
<div class="abs side more" style="top:1996px">Continue Reading...</div>
<div class="abs rule" style="top:2043px"></div>

<div class="abs ph" role="img" aria-label="Student studying at a desk" style="left:625px;top:2061px;width:127px;height:126px;background:linear-gradient(135deg,#d6d2c8,#8a7060);border-radius:0"></div>
<div class="abs side post-meta" style="top:2073px">&#9679; Plomvarinex &nbsp;&nbsp; | &nbsp; &#9719; Dec 18 ,2020</div>
<div class="abs side post-title" style="top:2098px">Lorem ipsum dolor sit amet, consectetur adipiscing</div>
<div class="abs side more" style="top:2159px">Continue Reading...</div>

<!-- ASK -->
<section class="abs ask" id="ask"></section>
<div class="abs ph" role="img" aria-label="Student with a laptop pointing toward the question form" style="left:229px;top:2213px;width:278px;height:391px;background:linear-gradient(180deg,#c46a5a 0%,#d9b79a 55%,#ece3d6 100%)"></div>
<div class="abs" style="left:550px;top:2255px;font-size:38px;font-weight:300"><span class="mini-cap"></span>Ask a <b style="font-weight:500">Job</b></div>
<div class="abs" style="left:547px;top:2290px;font-size:60px;font-weight:700;color:var(--heading-blue)">Question?</div>
<div class="abs field" style="left:550px;top:2368px;width:436px;height:44px;font-size:14px">Email Address</div>
<div class="abs field" style="left:550px;top:2425px;width:436px;height:77px;font-size:14px;align-items:flex-start;padding-top:14px">Job Question?</div>
<a class="abs btn" style="left:818px;top:2517px;width:175px;height:39px" href="#">Submit</a>

<!-- VOLUNTEER -->
<h2 class="abs sec-title" id="volunteer" style="top:2658px"><span class="cap"></span>Volunteer <b>Opportunities</b></h2>
<svg class="abs" style="left:74px;top:2840px" width="18" height="28" aria-hidden="true"><path d="M14 2 L4 14 L14 26" fill="none" stroke="#333" stroke-width="2"/></svg>
<svg class="abs" style="left:1110px;top:2840px" width="18" height="28" aria-hidden="true"><path d="M4 2 L14 14 L4 26" fill="none" stroke="#333" stroke-width="2"/></svg>

<div class="abs card vcard" style="left:101px;top:2741px"><div class="hd"><i class="logo" style="background:#dfe9f7"></i><div><div class="name">Business Name</div><div class="loc">&#9679; Location Name</div></div></div><p>Lorem ipsum dolor sit amet,adipi sed do eiusmod tempor incididunt utbore et dmagna aliqua.Lorem ipsum dolor sit Lorem ipsum dolor sit amet,adipis Lorem ipsum dolor sit amet,adipislit</p><div class="ft"><a class="visit" href="#">Contact Info &raquo;</a><span class="time"></span><span class="dots">&bull;&bull;&bull;</span></div></div>
<div class="abs card vcard" style="left:440px;top:2741px"><div class="hd"><i class="logo"></i><div><div class="name">Business Name</div><div class="loc">&#9679; Location Name</div></div></div><p>Lorem ipsum dolor sit amet,adipi sed do eiusmod tempor incididunt utbore et dmagna aliqua.Lorem ipsum dolor sit Lorem ipsum dolor sit amet,adipis Lorem ipsum dolor sit amet,adipislit</p><div class="ft"><a class="visit" href="#">Contact Info &raquo;</a><span class="time"></span><span class="dots">&bull;&bull;&bull;</span></div></div>
<div class="abs card vcard" style="left:778px;top:2741px"><div class="hd"><i class="logo" style="background:#2f3cbf"></i><div><div class="name">Business Name</div><div class="loc">&#9679; Location Name</div></div></div><p>Lorem ipsum dolor sit amet,adipi sed do eiusmod tempor incididunt utbore et dmagna aliqua.Lorem ipsum dolor sit Lorem ipsum dolor sit amet,adipis Lorem ipsum dolor sit amet,adipislit</p><div class="ft"><a class="visit" href="#">Contact Info &raquo;</a><span class="time"></span><span class="dots">&bull;&bull;&bull;</span></div></div>

<!-- ABOUT -->
<div class="abs about-bg"></div>
<div class="abs" style="left:1170px;top:3110px;transform:rotate(90deg);transform-origin:left top;font-size:78px;font-weight:700;color:rgba(0,0,0,.05);white-space:nowrap">ABOUT US</div>
<div class="abs" style="left:1157px;top:3340px;width:16px;height:16px;border-radius:50%;background:var(--orange)"></div>
<div class="abs ph" role="img" aria-label="Smiling young woman with arms crossed" style="left:180px;top:3107px;width:425px;height:614px;background:linear-gradient(180deg,#5a3a2a 0%,#d9b49a 30%,#6e6a66 55%,#5f5b58 100%);border-radius:0"></div>
<div class="abs" style="left:44px;top:3246px;width:180px;font-size:13px;font-weight:500;line-height:16px;color:#333">"Trovique Staffing helped me land my dream job!"<div style="font-size:8px;font-weight:400;line-height:10px;margin-top:3px">Candidate, Business Analyst,<br>Transportation company, Corvale, ST</div></div>

<h2 class="abs" id="about" style="left:687px;top:3125px;font-size:39px;font-weight:300"><span class="mini-cap"></span>About <b style="font-weight:500;color:var(--heading-blue)">Us</b></h2>
<div class="abs about" style="left:690px;top:3181px;width:415px">
  <p>Lorem ipsum dolor sit amet, consectetur adscing elit, sed do eiusmod tempor incididunt ut labore et dolore magna aliqua. Quis ispendisse ultrices gravida. Risus commodo viverrcenas accumsan lacus vel facilisis. Lorem ipsum dolor sit amet, cectetur adipiscing elit, sed do eiusmod tempor incididunt ut labore et dolore magna aliqua. Quis ipsum suspendisse ultrices gravida</p>
  <p style="margin-top:18px">Lorem ipsum dolor sit amet, consectetur adscing elit, sed do eiusmod tempor incididunt ut labore et dolore magna aliqua. Quis ispendisse ultrices gravida. Risus commodo viverrcenas accumsan lacus vel facilisis. Lorem ipsum dolor sit amet, cectetur adipiscing elit, sed do eiusmod tempor incididunt</p>
</div>
<a class="abs btn" style="left:690px;top:3508px;width:174px;height:43px" href="#">Learn More</a>

<!-- FOOTER -->
<svg class="abs footer" viewBox="0 0 1200 513" width="1200" height="513" aria-hidden="true">
  <defs><linearGradient id="fg" x1="0" y1="0" x2="0" y2="1"><stop offset="0" stop-color="#7fd3f1"/><stop offset=".35" stop-color="#3dbfea"/><stop offset="1" stop-color="#2ab5e4"/></linearGradient></defs>
  <path d="M0 40 C220 10 420 60 640 45 C860 30 1020 10 1200 30 L1200 513 L0 513Z" fill="url(#fg)"/>
  <path d="M0 20 C300 50 600 0 900 20 C1050 30 1130 10 1200 15 L1200 40 C1020 10 860 30 640 45 C420 60 220 10 0 40Z" fill="rgba(127,211,241,.4)"/>
  <rect x="101" y="454" width="998" height="1" fill="rgba(255,255,255,.6)"/>
</svg>
<div class="abs fcol" style="left:101px;top:3928px"><h4>Quick Links</h4><a href="#jobs">Job Opportunities</a><a href="#tools">Tools &amp; Career Advice</a><a href="#ask">&nbsp;Ask a Job Question?</a><a href="#volunteer">Volunteer Opportunities</a><a href="#about">About Us</a></div>
<div class="abs fcol" style="left:365px;top:3928px"><h4>Other Links</h4><a href="#">Privacy Policy</a><a href="#">Terms of Service</a><a href="#">Credit</a><a href="#">FAQ</a></div>
<div class="abs fcol" style="left:581px;top:3928px"><h4>Contact Us</h4>
  <div class="contact"><span class="ic"><svg width="14" height="18" viewBox="0 0 14 18"><path d="M7 1a6 6 0 0 0-6 6c0 4.5 6 10 6 10s6-5.5 6-10a6 6 0 0 0-6-6z" fill="none" stroke="#fff" stroke-width="1.5"/><circle cx="7" cy="7" r="2" fill="#fff"/></svg></span><span>88 Larkmoor Lane Fenwick<br>USA &nbsp;40417</span></div>
  <div class="contact"><span class="ic"><svg width="16" height="16" viewBox="0 0 16 16"><path d="M3 1l3 3-2 2c1 2 3 4 5 5l2-2 3 3-2 3C6 14 2 10 1 3z" fill="none" stroke="#fff" stroke-width="1.4"/></svg></span><span>555-014-2290</span></div>
  <div class="contact"><span class="ic"><svg width="16" height="12" viewBox="0 0 16 12"><rect x="1" y="1" width="14" height="10" fill="none" stroke="#fff" stroke-width="1.4"/><path d="M1 1l7 6 7-6" fill="none" stroke="#fff" stroke-width="1.4"/></svg></span><span>info@plomvarinex.com</span></div>
</div>
<div class="abs brand" style="left:924px;top:3990px;font-size:22px"><span class="dot"></span><span>plomvarinex.com<small>Jobs | Tools | Success</small></span></div>
<div class="abs" style="left:915px;top:4082px;display:flex;gap:11px">
  <a class="social" href="#" aria-label="Social profile 1"></a>
  <a class="social" href="#" aria-label="Social profile 2"></a>
  <a class="social" href="#" aria-label="Social profile 3"></a>
  <a class="social" href="#" aria-label="Social profile 4"></a>
</div>
<div class="abs" style="left:0;top:4177px;width:1200px;text-align:center;color:var(--white);font-size:13px">Copyright &copy; 2021 Plomvarinex. All rights reserved.</div>

</body>
</html>
```